Option Sheet

We need a one page option sheet with a left to right reading of the five options. It should be a one sheet, multiple colors and definitive separations between options This is used in a sales consultation. Backround or colors not in option need to have the follow RGB value (5 red, 20 green, 63 blue)

We added a smaller text file, please change that point

Target Market(s)

Divorce

Industry/Entity Type

Legal

Requirements
Must have
• 1) All five options left to right
• 2)language included in sheet

```html
<!DOCTYPE html>
<html lang="en">
<head>
<meta charset="utf-8">
<title>Five Options – Divorce</title>
<link href="https://fonts.googleapis.com/css2?family=Bebas+Neue&family=Oswald:wght@500;700&family=Roboto:wght@400;500&display=swap" rel="stylesheet">
<style>
  :root {
    --navy: rgb(5, 20, 63);
    --navy-tile: rgba(60, 78, 150, 0.35);
    --orange: #e3861b;
    --white: #ffffff;
  }
  * { box-sizing: border-box; margin: 0; padding: 0; }
  html, body { width: 1150px; height: 1200px; overflow: hidden; }
  body { background: var(--white); font-family: "Roboto", Arial, sans-serif; }

  .sheet { width: 1150px; height: 1200px; position: relative; background: var(--white); overflow: hidden; }

  .masthead { height: 160px; position: relative; }
  .masthead__title {
    position: absolute; left: 80px; top: 28px;
    font-family: "Bebas Neue", "Oswald", sans-serif; font-weight: 400;
    font-size: 148px; line-height: 1; letter-spacing: 1px;
  }
  .masthead__title .accent { color: var(--orange); }
  .masthead__title .strong { color: var(--navy); }
  .masthead__band {
    position: absolute; right: 0; top: 108px; width: 330px; height: 32px;
    background: var(--orange);
  }
  .masthead__web {
    position: absolute; right: 80px; top: 82px;
    font-family: "Roboto", Arial, sans-serif; font-weight: 500;
    font-size: 19px; color: var(--navy);
  }
  .masthead__topic {
    position: absolute; right: 80px; top: 108px;
    font-family: "Oswald", sans-serif; font-weight: 500;
    font-size: 26px; line-height: 32px; letter-spacing: 8px; color: var(--navy);
  }

  .options {
    position: absolute; top: 160px; left: 0; right: 0; height: 1010px;
    display: grid; grid-template-rows: repeat(5, minmax(0, 1fr)); row-gap: 5px;
  }

  .option { position: relative; display: grid; grid-template-columns: 80px 6px 1fr; min-height: 0; }
  .option__tab { background: var(--orange); position: relative; }
  .option__tab::after {
    content: ""; position: absolute; right: -16px; top: 50%; margin-top: -14px;
    border-left: 16px solid var(--orange); border-top: 14px solid transparent;
    border-bottom: 14px solid transparent; z-index: 2;
  }
  .option__label {
    position: absolute; left: 50%; top: 50%;
    transform: translate(-50%, -50%) rotate(-90deg);
    font-family: "Oswald", sans-serif; font-weight: 700; font-size: 28px;
    letter-spacing: 1px; color: var(--navy); white-space: nowrap;
  }
  .option__gap { background: var(--white); }
  .option__panel { background: var(--navy); position: relative; padding: 20px 0 0 170px; overflow: hidden; }
  .option__number {
    position: absolute; left: 50px; top: 50%; transform: translateY(-50%);
    font-family: "Oswald", sans-serif; font-weight: 500; font-size: 70px; line-height: 1; color: var(--white);
  }
  .option__title {
    font-family: "Bebas Neue", "Oswald", sans-serif; font-weight: 400; font-size: 24px;
    color: var(--orange); letter-spacing: 1px; line-height: 1; margin-bottom: 9px;
  }
  .option__tag {
    display: inline-block; background: var(--white); color: var(--navy);
    font-family: "Oswald", sans-serif; font-weight: 500; font-size: 11px;
    padding: 0 4px; letter-spacing: 0.5px; line-height: 14px;
  }
  .option__list { list-style: none; margin: 4px 0 7px 18px; }
  .option__list li {
    color: var(--white); font-size: 12px; line-height: 14.5px; position: relative; padding-left: 12px;
    max-width: 620px;
  }
  .option__list li::before { content: "•"; position: absolute; left: 0; }

  .deco { position: absolute; right: 40px; top: 50%; transform: translateY(-50%); }
</style>
</head>
<body>
<main class="sheet">
  <header class="masthead">
    <h1 class="masthead__title"><span class="accent">Five</span> <span class="strong">Options</span></h1>
    <div class="masthead__band"></div>
    <p class="masthead__web">WWW.KESTRELFAMILYLAW.COM</p>
    <p class="masthead__topic">DIVORCE</p>
  </header>

  <section class="options">
    <article class="option">
      <div class="option__tab"><span class="option__label">OPTION</span></div>
      <div class="option__gap"></div>
      <div class="option__panel">
        <span class="option__number">1</span>
        <h2 class="option__title">Do Nothing</h2>
        <span class="option__tag">ADVANTAGES</span>
        <ul class="option__list"><li>Stay married</li><li>No life Changes</li></ul>
        <span class="option__tag">DISADVANTAGES</span>
        <ul class="option__list"><li>Remain unhappy, depressed, anxious</li><li>Money and assets may disappear</li><li>What is going to change?</li></ul>
        <svg class="deco" width="130" height="140" viewBox="0 0 140 150" aria-hidden="true">
          <rect x="55" y="0" width="85" height="85" fill="var(--navy-tile)"/>
          <rect x="0" y="60" width="34" height="34" fill="var(--navy-tile)"/>
          <rect x="0" y="116" width="34" height="34" fill="var(--navy-tile)"/>
          <rect x="55" y="116" width="34" height="34" fill="var(--navy-tile)"/>
        </svg>
      </div>
    </article>

    <article class="option">
      <div class="option__tab"><span class="option__label">OPTION</span></div>
      <div class="option__gap"></div>
      <div class="option__panel">
        <span class="option__number">2</span>
        <h2 class="option__title">Go to Counseling</h2>
        <span class="option__tag">ADVANTAGES</span>
        <ul class="option__list"><li>Reconcile marriage</li><li>Help make a better life</li></ul>
        <span class="option__tag">DISADVANTAGES</span>
        <ul class="option__list"><li>Past issues are highlighted and may drudge up old wounds</li><li>It may just clarify the reasons you need to separate and/or divorce</li><li>Both parties must be invested and willing to participate</li></ul>
        <svg class="deco" width="54" height="120" viewBox="0 0 58 130" aria-hidden="true">
          <polygon points="29,0 58,26 0,26" fill="var(--orange)"/>
          <polygon points="29,52 58,78 0,78" fill="var(--orange)"/>
          <polygon points="29,104 58,130 0,130" fill="var(--orange)"/>
        </svg>
      </div>
    </article>

    <article class="option">
      <div class="option__tab"><span class="option__label">OPTION</span></div>
      <div class="option__gap"></div>
      <div class="option__panel">
        <span class="option__number">3</span>
        <h2 class="option__title">Do It Yourself</h2>
        <span class="option__tag">ADVANTAGES</span>
        <ul class="option__list"><li>No attorney fees</li></ul>
        <span class="option__tag">DISADVANTAGES</span>
        <ul class="option__list"><li>People often find that what is “fair,” may in fact, not be truly fair</li><li>Often times, people do not know the risks</li><li>Complicated legal system</li><li>Unsure how to complete the necessary paperwork and meet the deadlines</li></ul>
        <svg class="deco" width="130" height="140" viewBox="0 0 140 150" aria-hidden="true">
          <rect x="55" y="0" width="85" height="85" fill="var(--navy-tile)"/>
          <rect x="0" y="60" width="34" height="34" fill="var(--navy-tile)"/>
          <rect x="0" y="116" width="34" height="34" fill="var(--navy-tile)"/>
          <rect x="55" y="116" width="34" height="34" fill="var(--navy-tile)"/>
        </svg>
      </div>
    </article>

    <article class="option">
      <div class="option__tab"><span class="option__label">OPTION</span></div>
      <div class="option__gap"></div>
      <div class="option__panel">
        <span class="option__number">4</span>
        <h2 class="option__title">Limited Representation</h2>
        <span class="option__tag">ADVANTAGES</span>
        <ul class="option__list"><li>Balance between going alone and our limited involvement in the case</li></ul>
        <span class="option__tag">DISADVANTAGES</span>
        <ul class="option__list"><li>Our terms may not benefit from our legal knowledge</li><li>The legal consequences of your legal documents will not be explained to you so that you can formulate a plan for handling the rest of your case.</li><li>Your spouse or other parties may cause your legal fees to increase significantly without action on your part</li></ul>
        <svg class="deco" width="54" height="120" viewBox="0 0 58 130" aria-hidden="true">
          <polygon points="29,0 58,26 0,26" fill="var(--orange)"/>
          <polygon points="29,52 58,78 0,78" fill="var(--orange)"/>
          <polygon points="29,104 58,130 0,130" fill="var(--orange)"/>
        </svg>
      </div>
    </article>

    <article class="option">
      <div class="option__tab"><span class="option__label">OPTION</span></div>
      <div class="option__gap"></div>
      <div class="option__panel">
        <span class="option__number">5</span>
        <h2 class="option__title">Hire Us</h2>
        <span class="option__tag">ADVANTAGES</span>
        <ul class="option__list"><li>Gain the full benefits of our experience</li><li>Have a team of Kestrel Family Law attorneys</li><li>Often saves you money in the long run</li><li>Save you time and energy</li></ul>
        <span class="option__tag">DISADVANTAGES</span>
        <ul class="option__list"><li>Initial Cost</li></ul>
        <svg class="deco" width="130" height="140" viewBox="0 0 140 150" aria-hidden="true">
          <rect x="55" y="0" width="85" height="85" fill="var(--navy-tile)"/>
          <rect x="0" y="60" width="34" height="34" fill="var(--navy-tile)"/>
          <rect x="0" y="116" width="34" height="34" fill="var(--navy-tile)"/>
          <rect x="55" y="116" width="34" height="34" fill="var(--navy-tile)"/>
        </svg>
      </div>
    </article>
  </section>
</main>
</body>
</html>
```